Tru-Level Building Inspections Flyer Design

We need a flyer design for our building inspections company based in Perth, Western Australia. We conduct pre-purchase building, timber pest and pool barrier safety inspections. We would like to see designs that use the colours black, grey & red. I have attached our effort on design although this is far to busy and needs better imagery. For further information on our services etc. please visit www.tru-levelbuildinginspections.example.au or contact us via our e-mail if you require any further photography (such as action shots, us with our signwritten vehicles etc.).

Industry/Entity Type

It Company

Requirements
Must have
• logo at top of page with Tru-Level Building Inspections title.
Nice to have
• Inspector Photo
• The "Providing you with quality information about your property using
• Specialised Reporting Systems" in a banner linked with the photo. Also to be in an easily readable italic font.
Should not have
• The norbelle star/discount picture on the uploaded flyer.
• Also the paragraph "The Tru-Level Comprehensive Pre-Purchase/Sale Building Inspection has been uniquely designed to ensure you are given as much relevant information as possible to empower you to make the best informed decisions with regard to your property" is no longer required.

```html
<!DOCTYPE html>
<html lang="en">
<head>
<meta charset="utf-8">
<title>Tru-Level Building Inspections</title>
<link rel="stylesheet" href="https://fonts.googleapis.com/css2?family=Open+Sans:ital,wght@0,400;0,600;0,700;0,800;1,400&display=swap">
<style>
:root{
  --red:#c0202f;
  --red-deep:#9e1622;
  --red-bright:#d8283a;
  --black:#1a0a0c;
  --ink:#333;
  --white:#fff;
  --sky-top:#b9cde0;
  --sky-mid:#8fa8c0;
  --water:#4d6680;
}
*{box-sizing:border-box;margin:0;padding:0}
html,body{width:846px;height:1200px;overflow:hidden;background:#fff}
body{font-family:"Open Sans",Arial,sans-serif;color:var(--ink)}
.flyer{position:relative;width:846px;height:1200px;overflow:hidden;background:#fff}
.masthead{position:absolute;left:0;top:0;width:846px;height:92px;
  background:linear-gradient(90deg,var(--black) 0%,var(--red) 35%,var(--red) 65%,var(--black) 100%);
  display:flex;align-items:center;justify-content:center;gap:14px}
.masthead .mark{width:24px;height:24px;background:var(--white);display:block}
.masthead h1{color:var(--white);font-weight:800;font-size:39px;letter-spacing:.3px;white-space:nowrap}
.services{position:absolute;left:40px;top:150px;list-style:none;width:420px}
.services li{position:relative;padding-left:30px;color:var(--red);font-weight:700;font-size:24px;line-height:35px;letter-spacing:.3px}
.services li::before{content:"";position:absolute;left:0;top:9px;width:16px;height:16px;background:var(--red)}
.tagline{position:absolute;left:476px;top:117px;width:370px;height:125px;background:var(--red);
  border-radius:18px 0 0 18px;color:var(--white);font-weight:700;font-size:19.5px;line-height:24px;padding:11px 20px 0 43px}
.features{position:absolute;left:40px;top:425px;width:770px;display:flex}
.feature{width:192px;text-align:center}
.feature svg{width:100px;height:100px;display:block;margin:0 auto 14px}
.feature p{font-size:12px;line-height:14.5px;color:#333;white-space:nowrap}
.pill{position:absolute;left:40px;top:628px;width:300px;height:50px;border-radius:25px;
  background:linear-gradient(180deg,var(--red-bright),var(--red-deep));box-shadow:3px 3px 0 var(--black);
  color:var(--white);font-weight:800;font-size:22px;line-height:50px;padding-left:27px}
.about{position:absolute;left:47px;top:688px;width:780px;color:var(--red);font-size:17px;line-height:21px;white-space:nowrap}
.divider{position:absolute;left:0;top:790px;width:846px;height:16px;background:linear-gradient(90deg,var(--black),var(--red) 50%,var(--black))}
.city{position:absolute;left:0;top:806px;width:846px;height:394px;
  background:linear-gradient(180deg,var(--sky-top) 0%,var(--sky-mid) 55%,#6f7f8c 75%,var(--water) 100%)}
.brand{position:absolute;left:44px;top:980px;display:flex;align-items:center;gap:10px}
.brand .mark{width:22px;height:22px;background:var(--red);display:block}
.brand span{font-size:40px;font-weight:600;color:var(--black)}
.contact{position:absolute;left:40px;top:1062px;color:var(--white);font-size:16px;line-height:24px;font-style:normal}
.contact b{font-weight:700}
.social{position:absolute;left:636px;top:1084px;text-align:center;color:var(--white);font-size:14px}
.social .squares{display:flex;gap:6px;margin-bottom:6px}
.social .squares i{width:30px;height:30px;background:var(--red);display:block}
</style>
</head>
<body>
<svg width="0" height="0" style="position:absolute">
  <defs>
    <symbol id="burst" viewBox="0 0 100 100">
      <polygon points="98,50 90.6,60.9 91.6,74 79.7,79.7 74,91.6 60.9,90.6 50,98 39.1,90.6 26,91.6 20.3,79.7 8.4,74 9.4,60.9 2,50 9.4,39.1 8.4,26 20.3,20.3 26,8.4 39.1,9.4 50,2 60.9,9.4 74,8.4 79.7,20.3 91.6,26 90.6,39.1"/>
    </symbol>
  </defs>
</svg>
<div class="flyer">
  <header class="masthead"><i class="mark"></i><h1>TRU-LEVEL BUILDING INSPECTIONS</h1></header>

  <ul class="services">
    <li>COMPREHENSIVE BUILDING INSPECTIONS</li>
    <li>STRUCTURAL INSPECTIONS</li>
    <li>TIMBER PEST/TERMITE INSPECTIONS</li>
    <li>SWIMMING POOL/SPA SAFETY BARRIER INSPECTIONS</li>
  </ul>

  <div class="tagline">Providing you with quality information about your property using&nbsp; Specialised Reporting Systems</div>

  <section class="features">
    <div class="feature">
      <svg viewBox="0 0 100 100"><use href="#burst" fill="var(--red)"/>
        <circle cx="50" cy="50" r="20" fill="none" stroke="#fff" stroke-width="3"/>
        <path d="M40 42c2-3 5-3 6 0l2 4-3 3c2 4 4 6 8 8l3-3 4 2c3 1 3 4 0 6-8 3-22-11-20-20z" fill="#fff"/>
        <text x="53" y="46" font-size="11" font-weight="700" fill="#fff" font-family="Open Sans,sans-serif">24</text>
      </svg>
      <p>You will be sent you<br>report within<br>24 hours of the inspection</p>
    </div>
    <div class="feature">
      <svg viewBox="0 0 100 100"><use href="#burst" fill="var(--red)"/>
        <rect x="36" y="28" width="28" height="42" rx="4" fill="none" stroke="#fff" stroke-width="3"/>
        <path d="M52 52v14h10v-8z" fill="#fff"/>
      </svg>
      <p>You will always be contacted<br>after your inspection to ensure<br>you fully understand<br>the contents of your report</p>
    </div>
    <div class="feature">
      <svg viewBox="0 0 100 100"><use href="#burst" fill="var(--red)"/>
        <rect x="31" y="31" width="17" height="17" fill="#fff"/><rect x="52" y="31" width="17" height="17" fill="#fff"/>
        <rect x="31" y="52" width="17" height="17" fill="#fff"/><rect x="52" y="52" width="17" height="17" fill="#fff"/>
        <path d="M35 39.5h9M39.5 35v9M56 39.5h9M35 60.5h9M56 58h9M56 63h9" stroke="var(--red)" stroke-width="2.5"/>
      </svg>
      <p>We utilize the very latest<br>state-of-the-art equipment<br>and tools including thermal<br>imaging cameras and the<br>Termascan T5 to assist us in<br>providing you with the most<br>accurate and comprehensive<br>property reports</p>
    </div>
    <div class="feature">
      <svg viewBox="0 0 100 100"><use href="#burst" fill="var(--red)"/>
        <rect x="30" y="36" width="40" height="28" rx="3" fill="none" stroke="#fff" stroke-width="3"/>
        <circle cx="43" cy="47" r="6" fill="#fff"/>
        <path d="M52 47h12M52 54h10" stroke="#fff" stroke-width="2.5"/>
      </svg>
      <p>Highly trained and<br>experienced team with the<br>ability to produce individually<br>tailored reports<br>in swift turnaround times</p>
    </div>
  </section>

  <div class="pill">WE WORK FOR YOU!</div>

  <p class="about">Tru-Level Building Inspections is a boutique, family run business which work in YOUR best<br>interests! We aim to provide an efficient, hassle-free service which provides<br>sufficient advice and information to empower you with the knowledge<br>to proceed confidently in your transactions.</p>

  <div class="divider"></div>

  <div class="city" role="img" aria-label="Photograph of the Perth city skyline across the river"></div>

  <div class="brand"><i class="mark"></i><span>Tru-Level</span></div>

  <address class="contact">
    Tel: <b>(08) 5550 1234</b><br>
    Email: <b>enquiries@tru-levelbuildinginspections.example.au</b><br>
    Web: <b>www.tru-levelbuildinginspections.example.au</b><br>
    Address: <b>Suite 8/22 Marlow Parade, Kinross WA 6028</b>
  </address>

  <div class="social">
    <div class="squares"><i></i><i></i><i></i><i></i></div>
    Follow us on Social Media
  </div>
</div>
</body>
</html>
```